Law Firm Website

I currently have a temporary site that I created myself at www.mcorveyfirm.net (hosted by 9tree). I am generally happy with the content.

My permanent website just has basic information right now: www.mcorveyfirm.com (hosted by lumenrack). I want to take the general content from the temporary website and have a more professional looking website on the permanent website. I want it in Wordpress format. I want a link to my blog: www.crookedpath.com. I want it to work on pads and smart phones. My number and e-mail address should be available on every page. The idea is to feature the potential client more than the lawyer.
Updates

Several of the designs are good. I would like the front page to have my number and address at the top (and at the top of every page) and to identify my law firm as "Law Office of Gerald T. Corvey". No need to include "mcorveyfirm" as that is just the web address. I like showing the most recent blog posts on the front page. I don't need video. No need to emphasize office hours or map location on the front page (that could be under a contact button). My picture should be somewhere. I would like an image from Boston on the front page if we can find one that is not copyright protected. No images of gavels or scales of justice. See some of the sample websites I listed in previous messages. Thanks!

Industry/Entity Type

Law Firm

```html
<!DOCTYPE html>
<html lang="en">
<head>
<meta charset="utf-8">
<title>Law Office of Gerald T. Corvey</title>
<link rel="stylesheet" href="https://fonts.googleapis.com/css2?family=Open+Sans:wght@400;600;700&family=Roboto+Slab:wght@400;700&display=swap">
<style>
:root{
  --ink:#2b2b2b;
  --dark:#1f2021;
  --dark2:#2e3032;
  --accent:#e0461f;
  --accent-dark:#b9381a;
  --blue:#2d6fa8;
  --muted:#777;
  --line:#e3e3e3;
  --paper:#ffffff;
  --bg:#f2f2f2;
}
*{box-sizing:border-box;margin:0;padding:0}
html,body{width:855px;height:1200px;overflow:hidden}
body{background:var(--bg);font-family:"Open Sans",Arial,sans-serif;color:var(--ink);font-size:9px;line-height:1.4}
.page{width:855px;height:1200px;position:relative;background:var(--bg)}
.wrap{width:660px;margin:0 auto;background:var(--paper)}
.site-header{background:var(--dark);height:58px;display:flex;align-items:center;justify-content:space-between;padding:0 16px}
.brand small{display:block;color:#fff;font-size:11px;font-family:"Roboto Slab",Georgia,serif}
.brand strong{display:block;color:var(--accent);font-size:19px;font-family:"Roboto Slab",Georgia,serif;font-weight:400;line-height:1.1}
.contact-bar{display:flex;gap:16px;align-items:center;color:#fff}
.contact-item{display:flex;align-items:center;gap:6px}
.contact-item .ic{width:22px;height:22px;border-radius:50%;background:var(--accent);display:flex;align-items:center;justify-content:center}
.contact-item small{display:block;font-size:8px;color:#bbb}
.contact-item b{font-size:14px;color:var(--accent);font-weight:700}
.contact-item span{font-size:10px}
.main-nav{display:flex;background:var(--dark2);padding:3px 6px;gap:3px}
.main-nav a{background:var(--accent);color:#fff;text-decoration:none;font-size:8.5px;font-weight:600;padding:4px 8px}
.hero{position:relative;height:275px;background:linear-gradient(160deg,#8c8a86 0%,#5b5956 45%,#3c3a38 100%)}
.hero .arrow{position:absolute;top:120px;width:20px;height:30px;display:flex;align-items:center;justify-content:center}
.hero .arrow.l{left:8px}.hero .arrow.r{right:8px}
.hero-caption{position:absolute;left:0;right:0;bottom:0;background:rgba(20,20,20,.85);color:#fff;font-size:9px;padding:7px 14px;text-transform:uppercase}
.content{display:flex;gap:16px;padding:14px 14px 10px}
.blog{flex:0 0 418px}
.sidebar{flex:1}
h2.section-title{font-size:10px;font-weight:700;text-transform:uppercase;padding-bottom:5px;border-bottom:2px solid var(--line);margin-bottom:8px}
.sidebar h2.section-title{color:var(--blue)}
.post{display:flex;gap:10px;padding:8px 0 10px;border-bottom:1px solid var(--line);height:172px}
.post .thumb{flex:0 0 88px;height:66px;background:linear-gradient(135deg,#b8b3aa,#7c7770)}
.post-body{flex:1}
.post h3{color:var(--accent);font-size:10.5px;font-weight:600;line-height:1.3;margin-bottom:3px}
.post .meta{color:var(--muted);font-size:7.5px;margin-bottom:4px}
.post p{font-size:8px;color:#555;line-height:1.45}
.btn{display:inline-block;background:var(--accent);color:#fff;font-size:7.5px;font-weight:700;padding:4px 9px;margin-top:7px;text-transform:uppercase}
.date-badge{flex:0 0 26px;height:26px;border:1px solid var(--line);border-radius:50%;display:flex;align-items:center;justify-content:center;font-size:9px;font-weight:700;color:#555}
.services{list-style:none;margin-bottom:14px}
.services li{font-size:8px;color:#444;padding:3px 0 3px 12px;position:relative;line-height:1.35}
.services li::before{content:"";position:absolute;left:2px;top:7px;width:4px;height:4px;background:var(--accent);border-radius:50%}
.about{display:flex;gap:8px;margin-bottom:14px}
.about .portrait{flex:0 0 82px;height:100px;background:linear-gradient(180deg,#8996a6,#3e4754)}
.about p{font-size:8px;color:#555}
.map{height:92px;background:linear-gradient(135deg,#e8e4d8,#d2d9c8)}
.office{font-size:8px;color:#444;margin-top:6px}
.office b{display:block;color:var(--ink)}
.office .hours{background:var(--accent);color:#fff;padding:5px 6px;margin-top:6px}
.site-footer{position:absolute;left:0;right:0;bottom:0;height:58px;background:var(--dark);color:#ccc}
.footer-inner{width:660px;margin:0 auto;display:flex;justify-content:space-between;padding:10px 14px}
.social small{display:block;font-size:8px;font-weight:700;color:#fff;margin-bottom:5px}
.social .dots{display:flex;gap:4px}
.social .dots i{width:16px;height:16px;background:#44474a;display:block}
.footer-links{text-align:right;font-size:8px}
.footer-links nav{color:#fff;font-weight:600;margin-bottom:4px}
</style>
</head>
<body>
<div class="page">
  <div class="wrap">
    <header class="site-header">
      <div class="brand"><small>Law Office of</small><strong>Gerald T. Corvey</strong></div>
      <div class="contact-bar">
        <div class="contact-item">
          <div class="ic"><svg width="12" height="12" viewBox="0 0 24 24"><path fill="#fff" d="M6.6 10.8a15.1 15.1 0 006.6 6.6l2.2-2.2c.3-.3.7-.4 1-.2 1.1.4 2.3.6 3.6.6.6 0 1 .4 1 1V20c0 .6-.4 1-1 1A17 17 0 013 4c0-.6.4-1 1-1h3.5c.6 0 1 .4 1 1 0 1.3.2 2.5.6 3.6.1.3 0 .7-.2 1z"/></svg></div>
          <div><small>Call us now</small><b>617 555-0142</b></div>
        </div>
        <div class="contact-item">
          <div class="ic"><svg width="12" height="12" viewBox="0 0 24 24"><path fill="#fff" d="M3 5h18v14H3z"/><path fill="none" stroke="#e0461f" stroke-width="2" d="M3 6l9 7 9-7"/></svg></div>
          <span>gcorvey@mcorveyfirm.com</span>
        </div>
      </div>
    </header>
    <nav class="main-nav">
      <a>Home</a><a>Why Hire Me?</a><a>Success Stories</a><a>Practice Areas</a><a>Representative Clients</a><a>Services Provided</a><a>Contact Us</a><a>How To Find Us</a>
    </nav>
    <section class="hero" role="img" aria-label="Photo of lawyers meeting with a client in an office">
      <span class="arrow l"><svg width="12" height="22" viewBox="0 0 12 22"><path d="M10 2L2 11l8 9" fill="none" stroke="#fff" stroke-width="2.5"/></svg></span>
      <span class="arrow r"><svg width="12" height="22" viewBox="0 0 12 22"><path d="M2 2l8 9-8 9" fill="none" stroke="#fff" stroke-width="2.5"/></svg></span>
      <div class="hero-caption">Welcome to our site</div>
    </section>
    <div class="content">
      <section class="blog">
        <h2 class="section-title">Latest Blog</h2>
        <article class="post">
          <div class="thumb" role="img" aria-label="Blog post photo"></div>
          <div class="post-body">
            <h3>You're Damned If You Don't Appropriately Respond to a Trip Review or Online Post</h3>
            <div class="meta">Posted January 15, 2015 in Lawsuits | By Gerald T. Corvey, 617 555-0142</div>
            <p>We live in many times for businesses. Any client with a computer and internet connection can say anything that they want about your business in an online review, on social media, etc. That can be unfortunately costly for today's private businesses. The trackbacks may</p>
            <span class="btn">Read more</span>
          </div>
          <div class="date-badge">17</div>
        </article>
        <article class="post">
          <div class="thumb" role="img" aria-label="Blog post photo"></div>
          <div class="post-body">
            <h3>You're Damned If You Don't Settle Meritorious Discrimination Cases</h3>
            <div class="meta">Posted January 8, 2015 in Discrimination, Lawsuits</div>
            <p>You defend a discrimination claim aggressively all the way to trial. The plaintiff wins a technical victory and gets only a small award of damages. So small, that it seems like a win for you. You can live with that, right? But now here comes the employee's attorney's petition for</p>
            <span class="btn">Read more</span>
          </div>
          <div class="date-badge">08</div>
        </article>
        <article class="post">
          <div class="thumb" role="img" aria-label="Blog post photo"></div>
          <div class="post-body">
            <h3>You're Damned If You Are Sexually Harassed With an Employer</h3>
            <div class="meta">Posted August 15, 2014 in Discrimination, Hiring and Firing, Lawsuits, Sexual Harassment</div>
            <p>But being obsessed and pursuing a relationship can be just as damning. Take the recently reported case at the State Fair Work Board (SFWB) v. Mystery Health. The employer is on the hook (subject to potential appeals) for a sizable award because the board found one of the company's senior staff repeated unwanted advances to a female employee, even though she repeatedly rejected</p>
            <span class="btn">Read more</span>
          </div>
          <div class="date-badge">15</div>
        </article>
        <article class="post">
          <div class="thumb" role="img" aria-label="Blog post photo"></div>
          <div class="post-body">
            <h3>Off topic – Enforcing a Subpoena at the SFWB</h3>
            <div class="meta">Posted July 23, 2014 in Lawsuits</div>
            <p>Y If a duly served witness fails to appear, ask the Hearing Officer for an Order appointing one (the attorney) as an agent of the Commission for the limited purpose of enforcing the subpoena. The order should state that the witness failed to appear and is in contempt of the Commission.</p>
            <span class="btn">Read more</span>
          </div>
          <div class="date-badge">23</div>
        </article>
      </section>
      <aside class="sidebar">
        <h2 class="section-title">Services Provided</h2>
        <ul class="services">
          <li>Defending and prosecuting lawsuits</li>
          <li>Defending SFWB and agency complaints and other agency filings</li>
          <li>Drafting/modifying noncompete agreements</li>
          <li>Draft/review/modify employee handbooks</li>
          <li>Draft/review/analyze employment offer letters and contracts</li>
          <li>Counsel on hiring and firing issues</li>
          <li>Consult on employment practices and policies</li>
          <li>Contract review and stock purchases, mergers and acquisitions, and sound out specialist for more complex transactions</li>
          <li>Represent clients in depositions, mediations, arbitrations, administrative hearings, and trials</li>
          <li>Advise on employment aspects of transactions</li>
          <li>Draft/review business contracts of all types</li>
          <li>Owner's Earnings</li>
          <li>Serve as outside general counsel</li>
        </ul>
        <h2 class="section-title">About Us</h2>
        <div class="about">
          <div class="portrait" role="img" aria-label="Portrait of attorney Gerald T. Corvey"></div>
          <p>Gerald Corvey's practice is focused on business law, employment and related disputes, helping clients with counseling, litigation and transactional work across the region.</p>
        </div>
        <h2 class="section-title">Contact Us</h2>
        <div class="map" role="img" aria-label="Street map showing the office location"></div>
        <div class="office">
          <b>Law Office of Gerald T. Corvey</b>
          48 Harbor Lane, 3rd Floor, Boston, MA 02110
          <div class="hours"><b>Office Hours</b>We can be reached during the following hours: Monday–Thursday 9am–5pm</div>
        </div>
      </aside>
    </div>
  </div>
  <footer class="site-footer">
    <div class="footer-inner">
      <div class="social"><small>STAY WITH US</small><div class="dots"><i></i><i></i><i></i><i></i></div></div>
      <div class="footer-links">
        <nav>HOME &nbsp;|&nbsp; ABOUT US &nbsp;|&nbsp; TERMS AND CONDITIONS &nbsp;|&nbsp; CONTACT US</nav>
        <div>© Law Office of Gerald T. Corvey</div>
      </div>
    </div>
  </footer>
</div>
</body>
</html>
```